Flyer-Design für eine Therapeutin
Zielgruppe
Ich bin Therapeutin und biete u.a. Massagen, Craniosacrale Integration, LebensenergieBeratung usw. an
Die Zielgruppe sind gesundheitsbewusste, selbstreflektierte Frauen und Männer mittleren Alters.
Aufgabenstellung
Ich stelle mir einen Wickelfalz Flyer in üblichem DIN A 4 Format vor, bin aber auch offen für Neues. Die Farben hätte ich gerne in grün, türkis, blau und lila/aubergine.

```html
<!DOCTYPE html>
<html lang="de">
<head>
<meta charset="utf-8">
<title>Flyer Wickelfalz – Hofgut am Lindenhang</title>
<link href="https://fonts.googleapis.com/css2?family=Saira+Condensed:wght@400;500;600&family=Allura&display=swap" rel="stylesheet">
<style>
  :root{
    --blue:#1a92d8;
    --blue-deep:#2f6cc4;
    --violet:#5a3fa6;
    --violet-soft:#6f55bd;
    --ink:#222226;
    --ink-soft:#4a4a52;
    --paper:#ffffff;
    --stage:#d9d9db;
    --sans:"Saira Condensed", "Arial Narrow", sans-serif;
    --script:"Allura", cursive;
  }
  *{box-sizing:border-box;margin:0;padding:0}
  html,body{width:1200px;height:600px;overflow:hidden;background:var(--stage)}
  body{position:relative;font-family:var(--sans);color:var(--ink)}

  .spread{position:absolute;top:95px;width:580px;height:410px;display:flex;box-shadow:0 4px 14px rgba(0,0,0,.18)}
  .spread--inside{left:10px}
  .spread--outside{left:610px}
  .panel{position:relative;width:193.33px;height:100%;overflow:hidden;background:var(--paper)}

  /* inside */
  .service{margin-bottom:7px}
  .service__bar{height:18px;background:linear-gradient(90deg,var(--violet),var(--blue));
    color:#fff;font-family:var(--script);font-size:15px;line-height:19px;padding-left:10px;width:92%;
    white-space:nowrap;overflow:hidden}
  .service__text{font-size:9.5px;line-height:11.5px;padding:4px 10px 0 12px;color:var(--ink)}
  .panel--services{padding-top:12px;background:linear-gradient(90deg,#fff 70%,#f0f0f2)}
  .panel--offers{background:linear-gradient(90deg,#ececee,#fff 40%);padding-top:16px}
  .panel--offers .service__bar{margin-left:auto;padding-left:0;padding-right:10px;text-align:right;width:88%}
  .panel--offers .service__text{text-align:right;padding-right:10px}
  .panel--offers .service{margin-bottom:14px}
  .panel--gift{background:linear-gradient(90deg,#d8d8dc,#f3f3f5 30%,#fff);padding:12px 11px 0}
  .pill{border-radius:14px;background:linear-gradient(90deg,var(--violet),var(--blue));color:#fff;
    text-align:center;font-size:10.5px;line-height:12.5px;padding:4px 6px;font-weight:500}
  .script-line{font-family:var(--script);color:var(--violet);font-size:14px;line-height:14px}
  .gift-text{font-size:9.2px;line-height:11px;margin-top:7px}
  .gift-text p{margin-bottom:7px}
  .photo-gift{position:absolute;left:193.33px;bottom:0;width:386.67px;height:148px;
    background:linear-gradient(160deg,#c8c6c4 0%,#7a5a44 35%,#d86a8c 65%,#e9b7c4 100%)}

  /* outside */
  .panel--about{background:linear-gradient(90deg,#fff,#ececee 75%,#d6d6da);padding:18px 12px 0}
  .about__title{font-family:var(--script);color:var(--violet);font-size:20px;font-weight:400}
  .portrait-round{position:absolute;right:10px;top:14px;width:58px;height:58px;border-radius:50%;
    border:4px solid var(--violet);background:radial-gradient(circle at 50% 45%,#d9a98e,#6b4a3a 70%)}
  .about__text{margin-top:36px;font-size:7.6px;line-height:10.4px;color:var(--ink-soft)}
  .about__text p{margin-bottom:9px}
  .panel--about .script-line{color:var(--blue-deep);font-size:13px;line-height:13px;margin-top:4px}
  .panel--about .pill{position:absolute;left:10px;right:10px;bottom:14px;font-size:10px}

  .panel--list{background:linear-gradient(165deg,var(--blue) 0%,var(--blue-deep) 30%,var(--violet) 65%,var(--violet-soft));color:#fff;padding:14px 10px 0;text-align:center}
  .list__title{font-size:13.5px;line-height:15px;font-weight:500}
  .offer-list{list-style:none;margin-top:22px;font-size:13px;line-height:16.4px;font-weight:500}
  .pill--white{background:#fff;color:var(--ink);margin-top:8px;font-size:9.5px}
  .panel--list .script-line{color:#fff;font-size:13px;line-height:13px;margin-top:12px;text-align:left}
  .contact{text-align:left;font-size:8.8px;line-height:11.5px;margin-top:10px;font-style:normal}

  .panel--cover{background:#fff}
  .photo-cover{position:absolute;left:0;top:40px;width:100%;height:235px;
    background:linear-gradient(160deg,#6b4a34,#a86f52 45%,#3f6f8a)}
  .cover-waves{position:absolute;left:0;top:0}
  .brand{position:absolute;right:14px;top:20px;display:flex;align-items:center;gap:5px;
    font-size:12px;font-weight:500;color:var(--ink)}
  .brand__dot{width:8px;height:8px;border-radius:50%;background:var(--blue)}
  .cover__title{position:absolute;right:14px;bottom:52px;font-size:30px;font-weight:400;color:var(--ink)}
  .cover__sub{position:absolute;right:14px;bottom:14px;font-family:var(--script);font-size:36px;color:var(--violet)}
</style>
</head>
<body>

<section class="spread spread--inside">
  <div class="panel panel--services">
    <div class="service"><div class="service__bar">Massagen</div>
      <p class="service__text">Herrlich wohltuende Massagen lösen die Anspannung des Alltags und sind Wellness für Körper und Seele. Auch mit ätherischen Ölen buchbar.</p></div>
    <div class="service"><div class="service__bar">Cranio-Sacrale Integration</div>
      <p class="service__text">Sanfte Körperberührungen aktivieren die natürlichen Heilmechanismen im Körper.</p></div>
    <div class="service"><div class="service__bar">SomatoEmotionale Entspannung</div>
      <p class="service__text">„Gewebeerinnerungen“ werden sanft und achtsam gelöst. Tiefe Entspannung auf körperlicher und geistiger Ebene.</p></div>
    <div class="service"><div class="service__bar">HerzZentrierte Therapie</div>
      <p class="service__text">Emotionale und spirituelle Heilung durch die Weisheit Ihres Herzens.</p></div>
    <div class="service"><div class="service__bar">Meditationen</div>
      <p class="service__text">Konzentration, Achtsamkeit und Ruhe werden gefördert, gleichzeitig tanken Sie Kraft und Energie.</p></div>
    <div class="service"><div class="service__bar">WorkIn</div>
      <p class="service__text">Entspannung und Ausgleich durch bewusste Atmung, auch zur Krankheitsprävention. Einzeln oder in der Gruppe.</p></div>
  </div>

  <div class="panel panel--offers">
    <div class="service"><div class="service__bar">LebensenergieBeratung</div>
      <p class="service__text">Richte Deinen Blick auf die Einheit von Körper, Geist und Seele und finde tiefen inneren Frieden.</p></div>
    <div class="service"><div class="service__bar">Deine Ressourcenbox</div>
      <p class="service__text">Deine Kraftbox enthält Dinge, die Dich stärken, äußerlich wie innerlich, … wie Fähigkeiten, Hobbies, Menschen, Gegenstände, Orte, Erinnerungen.</p></div>
    <div class="service"><div class="service__bar">Präventionstraining</div>
      <p class="service__text">Fördere schnell deine körperliche Gesundheit und setze deine Körperenergie wieder frei.</p></div>
  </div>

  <div class="panel panel--gift">
    <div class="pill">Informiere Dich jetzt über mein Angebot unter<br>0151–23456789</div>
    <p class="script-line" style="margin-top:9px">Lass Dich von Herz zu Herz berühren – lass deine Seele tanzen – weil Du Liebe bist!</p>
    <div class="gift-text">
      <p>Du möchtest deinem Herzensmenschen etwas Gutes tun und etwas ganz Besonderes schenken?</p>
      <p>Einen Gutschein für eine Massage oder eines meiner anderen Angebote kann dir jederzeit gerne in Printform oder auch online per Email zukommen lassen oder du kannst diesen direkt bei uns im Hofgut am Lindenhang aussuchen – gerne in einem handgemachten Filzherz als individuelle liebevolle Verpackung.</p>
    </div>
  </div>

  <div class="photo-gift" role="img" aria-label="Foto: Gutschein für eine Massage mit Filzherz, Kerze, Duftöl und Rose auf einem Holztisch"></div>
</section>

<section class="spread spread--outside">
  <div class="panel panel--about">
    <h2 class="about__title">Wer ich bin…</h2>
    <div class="portrait-round" role="img" aria-label="Rundes Porträtfoto der Therapeutin"></div>
    <div class="about__text">
      <p>Herzenskommunikation ist meine Stärke! Sport- und Physiotherapie – in Verbindung mit zahlreichen therapeutischen und persönlichen Weiterbildungen, meiner Lebenserfahrung sowie meiner intuitiven Kraft und Empathie ermöglichen es mir, Menschen nicht nur im Herzen zu spüren und wahrzunehmen, sondern tief im Herzen zu berühren – bis in ihren Wesenskern. Dies erlebe und spüre ich, wenn mich meine Klienten nach einer Therapieeinheit mit Tränen in den Augen ansehen und das wohlige Gefühl in sich tragen, zu tiefst entspannt und innerlich gesehen und wahrgenommen zu sein.</p>
      <p>Voller Dankbarkeit führe ich ein innerlich und äußerlich erfülltes Leben, was sich für jede/n erkennbar in unserem Wohnort im Hofgut am Lindenhang wieder spiegelt. Ein liebevoller Ort der Ruhe und der Kraft!</p>
      <p>Das Leben hat mich zu der gemacht, die ich heute bin. Meine Nahtoderfahrung nach einem Unfall hat mich zudem darin bestärkt, mich und meine Talente in die Welt einzubringen. Ich bin eine offene Frau, die ihre Kraft und Liebe gefunden hat.</p>
    </div>
    <p class="script-line">Lass Dich von Herz zu Herz berühren und lass deine Seele tanzen – weil Du Liebe bist!</p>
    <div class="pill">Nimm jetzt unverbindlich Kontakt mit mir auf!<br>Unter 0151–23456789</div>
  </div>

  <div class="panel panel--list">
    <h2 class="list__title">Fühle Dich tief berührt mit meinen wohltuenden Angeboten:</h2>
    <ul class="offer-list">
      <li>Massagen</li>
      <li>CranioSacrale Integration</li>
      <li>SomatoEmotionale Entspannung</li>
      <li>Herzzentrierte Therapie</li>
      <li>RessourcenBox</li>
      <li>LebensenergieBeratung</li>
      <li>Meditationen</li>
      <li>WorkIn</li>
      <li>Präventive Physiotherapie</li>
      <li>PräventionsTraining</li>
    </ul>
    <div class="pill pill--white">Jetzt Termin vereinbaren unter 0151–23456789</div>
    <p class="script-line">Lass Dich von Herz zu Herz berühren und lass deine Seele tanzen – weil Du Liebe bist!</p>
    <address class="contact">
      Lena Brandt<br>Birkenweg 7 | 12345 Musterdorf<br>info@hofgut-lindenhang.de<br>www.hofgut-lindenhang.de
    </address>
  </div>

  <div class="panel panel--cover">
    <div class="photo-cover" role="img" aria-label="Porträtfoto der lächelnden Therapeutin"></div>
    <svg class="cover-waves" width="194" height="410" viewBox="0 0 194 410" aria-hidden="true">
      <defs>
        <linearGradient id="waveGrad" x1="0" x2="1">
          <stop offset="0" stop-color="#5a3fa6"/><stop offset="1" stop-color="#2f6cc4"/>
        </linearGradient>
      </defs>
      <path d="M0 0H194V95C150 98 130 130 90 128C50 126 30 110 0 108Z" fill="url(#waveGrad)"/>
      <path d="M0 0H194V88C150 92 130 122 90 120C50 118 30 104 0 102Z" fill="#fff"/>
      <path d="M0 285C50 255 120 255 194 270V410H0Z" fill="url(#waveGrad)"/>
      <path d="M0 293C50 265 120 265 194 280V410H0Z" fill="#fff"/>
    </svg>
    <div class="brand"><span class="brand__dot"></span>Hofgut am Lindenhang</div>
    <h1 class="cover__title">Fühl Dich</h1>
    <p class="cover__sub">tief berührt!</p>
  </div>
</section>

</body>
</html>
```